RK Bastone Construction Inc.

Design a new business card for our construction company
To be removed from current card:
Delete 25 years
Delete Tenant fit up Renovations section

```html
<!DOCTYPE html>
<html lang="en">
<head>
<meta charset="utf-8">
<title>RK Bastone Construction Inc. – Business Card</title>
<link href="https://fonts.googleapis.com/css2?family=Montserrat:wght@400;500;700;800&display=swap" rel="stylesheet">
<style>
  :root {
    --backdrop: #999999;
    --card: #8c8c8a;
    --purple: #552d78;
    --teal: #237a6d;
    --ink: #262626;
  }
  * { margin: 0; padding: 0; box-sizing: border-box; }
  html, body {
    width: 1200px; height: 1059px; overflow: hidden;
    background: var(--backdrop);
    font-family: "Montserrat", sans-serif;
  }
  .card {
    position: absolute; left: 288px; width: 624px; height: 359px;
    background: var(--card);
    border-radius: 26px;
  }
  .card--front { top: 134px; }
  .card--back { top: 566px; }

  .wordmark {
    position: absolute; left: 0; right: 0;
    text-align: center;
    color: var(--purple);
    font-weight: 800;
    font-size: 40px;
    line-height: 1.15;
    letter-spacing: 1px;
    text-transform: uppercase;
  }
  .card--front .wordmark { top: 26px; }
  .card--back .wordmark { top: 130px; }

  .name-row {
    position: absolute; left: 25px; right: 25px; top: 204px;
    display: flex; align-items: center; gap: 10px;
  }
  .name-row .rule { flex: 1; height: 2px; background: var(--teal); }
  .person-name {
    font-weight: 700; font-size: 23px; letter-spacing: .5px;
    text-transform: uppercase; white-space: nowrap;
  }
  .person-name .first { color: var(--purple); }
  .person-name .last { color: var(--teal); }

  .contacts {
    position: absolute; left: 25px; top: 239px;
    list-style: none;
  }
  .contacts li {
    display: flex; align-items: center; gap: 8px;
    height: 23.5px;
    font-size: 16px; color: var(--ink);
  }
  .contacts svg { width: 14px; height: 14px; fill: var(--teal); flex: none; }

  .address {
    position: absolute; right: 25px; top: 286px;
    text-align: right; font-size: 16px; line-height: 23.5px; color: var(--ink);
    font-style: normal;
  }
</style>
</head>
<body>

<section class="card card--front">
  <div class="wordmark">RK Bastone<br>Construction Inc.</div>

  <div class="name-row">
    <span class="rule"></span>
    <h1 class="person-name"><span class="first">Luca</span> <span class="last">Bastone</span></h1>
    <span class="rule"></span>
  </div>

  <ul class="contacts">
    <li>
      <svg viewBox="0 0 16 16" aria-hidden="true"><path d="M1 6c0-2 3-3 7-3s7 1 7 3v1h-3V5.5H4V7H1zM3 8l2-2h6l2 2v5H3zm5 1.2a1.6 1.6 0 1 0 0 3.2 1.6 1.6 0 0 0 0-3.2z"/></svg>
      555-210-4433 ext: 118
    </li>
    <li>
      <svg viewBox="0 0 16 16" aria-hidden="true"><path d="M4.5 0h7a1 1 0 0 1 1 1v14a1 1 0 0 1-1 1h-7a1 1 0 0 1-1-1V1a1 1 0 0 1 1-1zm.5 2v10.5h6V2zm3 11.3a.9.9 0 1 0 0 1.8.9.9 0 0 0 0-1.8z"/></svg>
      555-384-7720
    </li>
    <li>
      <svg viewBox="0 0 16 16" aria-hidden="true"><path d="M1 3.5h14v1.2L8 9 1 4.7zM1 6.4l7 4.3 7-4.3V13H1z"/></svg>
      luca@rkbastoneconst.ca
    </li>
    <li>
      <svg viewBox="0 0 16 16" aria-hidden="true"><path d="M8 1a7 7 0 1 0 0 14A7 7 0 0 0 8 1zm-1 2.2c-.6 1-2 1.2-2 2.6 0 1.2 1.6 1 2 2.2.3 1-.8 2-.4 3.6L6 12.8A5.5 5.5 0 0 1 7 3.2zm3.4 1.1a5.5 5.5 0 0 1 2.4 6.4c-.8-.4-1-1.6-2-1.6-1 0-1.4-1.2-.8-2 .5-.7.2-1.8.4-2.8z"/></svg>
      www.rkbastoneconstruction.ca
    </li>
  </ul>

  <address class="address">1280 Harwood Rd.,Suite 200,<br>Kingston, ON K7L 4V3</address>
</section>

<section class="card card--back">
  <div class="wordmark">RK Bastone<br>Construction Inc.</div>
</section>

</body>
</html>
```